依頼詳細
■コンペで依頼するもの
・トップページ(ワイヤーフレーム参照)
■当選後に依頼するもの
・第2階層ページ(ワイヤーフレーム参照)
・記事ページ(ワイヤーフレーム参照)
・アイキャッチ画像6種類

当選後、追加依頼をプロジェクト形式で発注しますので、受注できる方でお願いします。
追加依頼の予算は4万円以内です。
サイトURL
http://www.morinoyashiro-sample.jp/wp/
ページ数
1ページ
希望イメージ
シンプル 複雑
単色 カラフル
暗い 明るい
日常 高級
遊び心 厳粛
未来的 伝統的
女性的 男性的
希望する色
背景は白指定です。他はお任せします。
納品ファイル
• フォトショップ形式 (.psd)
• PNG形式 (.png)
補足説明
■参考サイト
http://kotobukisha-example.or.jp/jingu/
http://www.hanazakura-example.or.jp/top.php
http://fukuo-mitama.or.jp/

■素材
添付のワイヤーフレームと写真です。
写真は次のアドレスからダウンロードしてください。
http://pelotix.net/morinoyashiro/sozai.zip
現行サイトの画像も利用して頂いて構いません。

※メニュー部の配置は自由にして頂いて構いません。
※ボックス内の文字は画像データとして利用します。他の文字はテキストデータで利用します。
※他有料素材も5千円程度まではお支払できます。

神紋(ロゴマーク)の色は自由に設定して頂いて構いません。
深緑以外であれば問題ないようです。
現行サイトのロゴには「北原郷総鎮守」が含まれています。
ですが、今回はトップページから削除することが決定しています。
説明が不足しておりまして申し訳ございません。
ワイヤーフレーム内、サイトマップのテキストは確定していません。
デザインが分かれば大丈夫です。ダミーのテキストを入れてください。
レスポンシブ対応とありますが、対応は当方で行います。
今回、PC版トップページのイメージアップが最優先ですので、
コンペではレスポンシブを意識せずにデザインして頂いて構いません。
よろしくお願いします。
23日(月) 14:00より選考を開始します。
一時停止の理由:たくさんのご提案を頂きましてありがとうございました。
現在クライアントを含めた席で協議中ですが、どれもクオリティが高く難航しています。
本日中には決定する見込みです。

全体の配色、写真の扱い方を考慮した結果、「クライアントのイメージに近い」という事で選択させて頂きました。

沢山のご提案、誠にありがとうございました。

```html
<!DOCTYPE html>
<html lang="ja">
<head>
<meta charset="utf-8">
<title>森之社 トップページ</title>
<link href="https://fonts.googleapis.com/css2?family=Noto+Serif+JP:wght@400;600;700&family=Noto+Sans+JP:wght@400;500&display=swap" rel="stylesheet">
<style>
:root{
  --navy:#24305a;
  --navy-dark:#1a2345;
  --gold:#a88440;
  --paper:#ffffff;
  --mist:#eef0f4;
  --line:#d6d9e0;
  --text:#33363d;
  --muted:#7b808b;
  --footer:#e9ebef;
  --forest-a:#5e7a5a;
  --forest-b:#a9b89c;
  --forest-c:#2f4530;
}
*{box-sizing:border-box;margin:0;padding:0}
html,body{width:857px;height:1200px;overflow:hidden;background:var(--paper);color:var(--text);font-family:"Noto Sans JP",sans-serif;font-size:9px;line-height:1.5}
.page{position:relative;width:857px;height:1200px;background:linear-gradient(180deg,#fff 0,#fff 60%,#f4f5f8 100%)}
a{color:inherit;text-decoration:none}

/* header & hero */
.hero{position:absolute;left:0;top:0;width:857px;height:362px;background:linear-gradient(180deg,#e9efe6 0%,var(--forest-b) 18%,var(--forest-a) 48%,var(--forest-c) 78%,#c9c1a8 100%)}
.brand{position:absolute;left:140px;top:42px;display:flex;align-items:center;gap:10px;font-family:"Noto Serif JP",serif;font-weight:700;font-size:30px;color:var(--navy-dark);letter-spacing:4px}
.brand-mark{width:26px;height:26px;border-radius:50%;background:var(--gold)}
.header-panel{position:absolute;left:0;top:0;width:857px;height:96px;background:linear-gradient(180deg,rgba(255,255,255,.95),rgba(255,255,255,.55))}
.tagline{position:absolute;top:14px;right:72px;display:flex;gap:6px;writing-mode:vertical-rl;font-family:"Noto Serif JP",serif;font-size:9px;color:var(--navy-dark);height:78px}
.tools{position:absolute;top:10px;right:18px;display:flex;gap:3px}
.tools span{display:block;width:14px;height:10px;background:var(--navy);opacity:.6}

/* global nav */
.global-nav{position:absolute;left:151px;top:385px;width:555px;height:28px;display:flex;background:var(--navy)}
.global-nav a{flex:1;display:flex;align-items:center;justify-content:center;color:#fff;font-family:"Noto Serif JP",serif;font-size:9.5px;border-right:1px solid rgba(255,255,255,.25)}
.global-nav a:last-child{border-right:0}
.global-nav a.is-current{background:var(--gold)}

/* sidebar */
.sidebar{position:absolute;left:151px;top:428px;width:148px}
.side-box{background:#fff;border:1px solid var(--line);padding:8px 10px 10px}
.side-box h3{font-family:"Noto Serif JP",serif;font-size:10px;color:var(--navy);border-bottom:1px solid var(--gold);padding-bottom:3px;margin-bottom:5px}
.side-box li{list-style:none;font-size:8px;color:var(--text);padding:2px 0 2px 9px;position:relative}
.side-box li::before{content:"";position:absolute;left:0;top:7px;width:4px;height:4px;background:var(--gold)}
.side-banner{margin-top:10px;height:58px;border:1px solid var(--line);display:flex;align-items:center;justify-content:center;font-family:"Noto Serif JP",serif;font-size:10px;color:#fff}
.side-banner.is-blue{background:linear-gradient(90deg,#3e6aa8,#8fb3dc)}
.side-banner.is-sky{background:linear-gradient(90deg,#5b8fc7,#c8dbee)}
.side-box.is-lower{margin-top:12px}

/* main */
.main{position:absolute;left:314px;top:428px;width:392px}
.feature-photo{height:116px;background:linear-gradient(135deg,#8fb0d8 0%,#c7d6e8 45%,#b8533e 70%,#3b4e78 100%)}
.news{margin-top:8px}
.news h2{font-family:"Noto Serif JP",serif;font-size:10px;color:var(--navy);border-bottom:1px solid var(--gold);padding-bottom:3px;margin-bottom:4px}
.news li{list-style:none;display:flex;gap:8px;font-size:8px;padding:3px 0;border-bottom:1px dotted var(--line)}
.news time{color:var(--gold);flex:0 0 52px}
.grid{margin-top:10px;display:grid;grid-template-columns:repeat(3,1fr);gap:10px 8px}
.card-head{height:16px;background:var(--navy);color:#fff;font-family:"Noto Serif JP",serif;font-size:8.5px;display:flex;align-items:center;justify-content:center}
.card-photo{height:66px}
.card p{font-size:7px;color:var(--muted);line-height:1.45;margin-top:4px}
.ph-1{background:linear-gradient(135deg,#c9a26a,#8d4a32)}
.ph-2{background:linear-gradient(135deg,#b9c6a4,#6e8a5f)}
.ph-3{background:linear-gradient(135deg,#d9cfa6,#b33a2c)}
.ph-4{background:linear-gradient(135deg,#7e9a6c,#3c5436)}
.ph-5{background:linear-gradient(135deg,#e6e2d6,#8e7a5e)}
.ph-6{background:linear-gradient(135deg,#a7b9c9,#566b82)}

/* footer */
.site-footer{position:absolute;left:0;top:968px;width:857px;height:232px;background:var(--footer);border-top:3px solid var(--navy)}
.sitemap{position:absolute;left:151px;top:18px;width:555px;display:grid;grid-template-columns:repeat(5,1fr);gap:0 10px}
.sitemap li{list-style:none;font-size:7.5px;color:var(--text);padding:2px 0}
.footer-brand{position:absolute;left:0;right:0;top:148px;display:flex;justify-content:center;align-items:center;gap:8px;font-family:"Noto Serif JP",serif;font-weight:700;font-size:20px;color:var(--navy-dark);letter-spacing:3px}
.footer-brand span{width:18px;height:18px;border-radius:50%;background:var(--gold)}
.copyright{position:absolute;left:0;right:0;top:182px;text-align:center;font-size:7px;color:var(--muted);line-height:1.6}
</style>
</head>
<body>
<div class="page">
  <header>
    <div class="hero" role="img" aria-label="杉木立が続く参道の写真"></div>
    <div class="header-panel"></div>
    <div class="brand"><span class="brand-mark"></span>森之社</div>
    <div class="tagline"><span>古き森に鎮まる社</span><span>北原郷総鎮守</span><span>ご参拝のご案内</span></div>
    <div class="tools"><span></span><span></span><span></span></div>
  </header>

  <nav class="global-nav">
    <a href="#" class="is-current">森之社のご紹介</a>
    <a href="#">祈願・お祓い</a>
    <a href="#">ご参拝のご案内</a>
    <a href="#">境内・見どころ</a>
    <a href="#">祭事・行事</a>
    <a href="#">交通</a>
  </nav>

  <aside class="sidebar">
    <div class="side-box">
      <h3>ご案内</h3>
      <ul>
        <li>初詣のご案内</li>
        <li>ご祈祷受付時間</li>
        <li>授与品のご案内</li>
        <li>宝物館のご案内</li>
        <li>境内案内図</li>
        <li>神前結婚式</li>
      </ul>
    </div>
    <div class="side-banner is-blue" role="img" aria-label="神前結婚式のバナー写真">神前結婚式</div>
    <div class="side-banner is-sky" role="img" aria-label="宝物館のバナー写真">宝物館</div>
    <div class="side-box is-lower">
      <h3>リンク</h3>
      <ul>
        <li>奉賛会</li>
        <li>関連神社</li>
        <li>お問い合わせ</li>
      </ul>
    </div>
  </aside>

  <main class="main">
    <div class="feature-photo" role="img" aria-label="御船祭の神輿船の写真"></div>
    <section class="news">
      <h2>最新情報</h2>
      <ul>
        <li><time>2015.03.10</time><span>春の例祭に関するお知らせを掲載しました</span></li>
        <li><time>2015.03.02</time><span>境内整備に伴う参道の通行についてご案内</span></li>
        <li><time>2015.02.20</time><span>宝物館の開館時間が変更となりました</span></li>
        <li><time>2015.02.11</time><span>紀元祭を斎行いたしました</span></li>
      </ul>
    </section>
    <section class="grid">
      <article class="card"><div class="card-head">由緒</div><div class="card-photo ph-1" role="img" aria-label="社殿の写真"></div><p>悠久の歴史を伝える社の由緒と御祭神をご紹介します。</p></article>
      <article class="card"><div class="card-head">御祭神</div><div class="card-photo ph-2" role="img" aria-label="神事の写真"></div><p>古くより人々に崇敬されてきた御祭神について。</p></article>
      <article class="card"><div class="card-head">祭事・行事</div><div class="card-photo ph-3" role="img" aria-label="楼門の写真"></div><p>年間を通して執り行われる祭事をご案内します。</p></article>
      <article class="card"><div class="card-head">境内</div><div class="card-photo ph-4" role="img" aria-label="境内の森の写真"></div><p>豊かな樹叢に包まれた境内の見どころです。</p></article>
      <article class="card"><div class="card-head">宝物館</div><div class="card-photo ph-5" role="img" aria-label="宝物館の建物の写真"></div><p>社に伝わる貴重な宝物を展示しています。</p></article>
      <article class="card"><div class="card-head">交通</div><div class="card-photo ph-6" role="img" aria-label="鳥居と参道の写真"></div><p>お車や電車でのアクセス方法をご案内します。</p></article>
    </section>
  </main>

  <footer class="site-footer">
    <ul class="sitemap">
      <li>森之社のご紹介</li><li>祈願・お祓い</li><li>ご参拝のご案内</li><li>境内・見どころ</li><li>祭事・行事</li>
      <li>由緒</li><li>厄除け</li><li>参拝作法</li><li>本殿</li><li>例祭</li>
      <li>御祭神</li><li>安産祈願</li><li>授与品</li><li>楼門</li><li>年中行事</li>
      <li>社殿</li><li>七五三</li><li>宝物館</li><li>御手洗池</li><li>交通</li>
    </ul>
    <div class="footer-brand"><span></span>森之社</div>
    <p class="copyright">〒000-0000 北原郷森之町1-1 TEL 000-000-0000<br>Copyright © 森之社 All Rights Reserved.</p>
  </footer>
</div>
</body>
</html>
```